Raising floral designer needs an artistic business card

I am an award winning floral designer wishing to transition from commercial wedding/event work to show designs as well as educating and consulting the art of flowers. My design style is the fusion of Ikebana and European floral art, so I wish my business card reflects it. I would like my card give people creative and energetic impression combined with the subtlety and gracefulness of the Eastern culture.
Target Market(s)
General public as well as related professionals
Industry/Entity Type
Floral
Contact Information for Business Card
Marla Juyin Pao BPGM, NLR.
Floral Artist and Consultant.
Phone: 555-719-2638.   email: marlafloral@quillmoor.com
Requirements
Must have
- color, floral/plant element, clean-looking
Nice to have
- a set with different color background/designs or shapes.
Should not have
- psychedelic colors and lines, illegible fonts.

```html
<!DOCTYPE html>
<html lang="en">
<head>
<meta charset="utf-8">
<title>Marla Juyin Pao — Floral Artist and Consultant</title>
<link rel="stylesheet" href="https://fonts.googleapis.com/css2?family=Bebas+Neue&family=Great+Vibes&family=Roboto+Condensed:wght@300&display=swap">
<style>
  :root {
    --bg-deep: #241a24;
    --bg-plum: #3a2538;
    --bloom: #6b3d66;
    --name: #dcc6f2;
    --ink: #f4eef6;
    --rule: #ffffff;
  }
  html, body {
    margin: 0;
    padding: 0;
    width: 1200px;
    height: 720px;
    overflow: hidden;
    background: var(--bg-deep);
  }
  .card {
    position: relative;
    width: 1200px;
    height: 720px;
    overflow: hidden;
  }
  .blossom-backdrop {
    position: absolute;
    inset: 0;
    background:
      radial-gradient(ellipse 420px 300px at 520px 420px, var(--bloom) 0%, rgba(107,61,102,0.35) 55%, rgba(107,61,102,0) 100%),
      radial-gradient(ellipse 300px 220px at 140px 380px, rgba(107,61,102,0.45) 0%, rgba(107,61,102,0) 100%),
      radial-gradient(ellipse 320px 240px at 1080px 80px, rgba(107,61,102,0.35) 0%, rgba(107,61,102,0) 100%),
      linear-gradient(180deg, var(--bg-plum) 0%, var(--bg-deep) 100%);
  }
  .frame-lines {
    position: absolute;
    inset: 0;
  }
  .name {
    position: absolute;
    left: 0;
    width: 1210px;
    top: 252px;
    margin: 0;
    text-align: center;
    font-family: "Bebas Neue", "Oswald", sans-serif;
    font-weight: 400;
    font-size: 84px;
    line-height: 1;
    letter-spacing: 1px;
    color: var(--name);
  }
  .role {
    position: absolute;
    left: 0;
    width: 1210px;
    top: 350px;
    margin: 0;
    text-align: center;
    font-family: "Great Vibes", cursive;
    font-size: 44px;
    line-height: 1;
    color: var(--ink);
  }
  .contact {
    position: absolute;
    top: 562px;
    margin: 0;
    font-family: "Roboto Condensed", "Arial Narrow", sans-serif;
    font-weight: 300;
    font-size: 38px;
    line-height: 1;
    color: var(--ink);
  }
  .contact--phone { left: 202px; }
  .contact--email { right: 204px; }
</style>
</head>
<body>
<main class="card">
  <div class="blossom-backdrop" role="img" aria-label="Blurred pink cherry blossom and aster arrangement on a dark plum background"></div>

  <svg class="frame-lines" width="1200" height="720" viewBox="0 0 1200 720" aria-hidden="false">
    <g class="rules" stroke="var(--rule)" stroke-width="2" fill="none">
      <line x1="160" y1="176" x2="544" y2="176"/>
      <line x1="656" y1="176" x2="1040" y2="176"/>
      <line x1="203" y1="192" x2="576" y2="192"/>
      <line x1="624" y1="192" x2="997" y2="192"/>
      <line x1="203" y1="608" x2="576" y2="608"/>
      <line x1="624" y1="608" x2="997" y2="608"/>
    </g>
    <rect class="ornament-top" x="443" y="70" width="314" height="100" rx="50" fill="rgba(244,238,246,0.12)" role="img" aria-label="Scrolled flourish ornament"/>
    <rect class="ornament-knot" x="578" y="182" width="44" height="20" rx="4" fill="rgba(244,238,246,0.55)" role="img" aria-label="Small diamond knot ornament"/>
    <rect class="ornament-knot" x="578" y="598" width="44" height="20" rx="4" fill="rgba(244,238,246,0.55)" role="img" aria-label="Small diamond knot ornament"/>
    <rect class="ornament-tip" x="147" y="170" width="34" height="12" rx="6" fill="rgba(244,238,246,0.55)" role="img" aria-label="Small arrow-tip ornament"/>
    <rect class="ornament-tip" x="1019" y="170" width="34" height="12" rx="6" fill="rgba(244,238,246,0.55)" role="img" aria-label="Small arrow-tip ornament"/>
  </svg>

  <h1 class="name">Marla Juyin Pao BPGM, NLR</h1>
  <p class="role">Floral Artist and Consultant</p>

  <p class="contact contact--phone">+555-719-2638</p>
  <p class="contact contact--email">marlafloral@quillmoor.com</p>
</main>
</body>
</html>
```